Business Card Design Project

We are a innovative residential building company based in Sydney, Australia
our business name is MORWEN CRAFTWORKS SOLUTIONS PTY LTD.
Our company by line (please incorporate) "Our Business is Building!"
We specialise in creating high end innovative residential Alterations & Additions for our clients.
We would like to see original high end designs that are professional, striking, creative & have the WOW factor...
We like BLACK, BLUE, ORANGE, WHITE, SILVER... We would like to convey to our clients - professionalism/innovative approach/design/creativity/assurance/wow factor...

Target Market(s)

Clients who want/need residential alterations or additions to their homes.

Industry/Entity Type

Residential

Requirements
Must have
• LOGO
Bi Line (somewhere)
Name
Title
Phone number
Email address

Member of the NHG (Northern Homecraft Guild) Logo
Web Address - www.morwencraftworks.com.au

Nice to have
• Fantail's are a small New Zealand bird and we would like to incorporate this as part of our new companies (double sided) business card. Whether it be the bird or just it's (fan) tail!
Should not have
• anything old-style.
we are looking for a contemporary, modern & striking Business Cards
clear strong colour accents
we had some stunning designs sent through, our favourites used the birds tail as an imprint on the card (not sure if that is clear of not)

```html
<!DOCTYPE html>
<html lang="en">
<head>
<meta charset="utf-8">
<title>Morwen Craftworks Solutions – Business Card</title>
<link href="https://fonts.googleapis.com/css2?family=Jost:wght@700&family=Arimo:wght@400;700&display=swap" rel="stylesheet">
<style>
  :root {
    --bg: #d0d0d0;
    --card-white: #ffffff;
    --brand-blue: #1591cf;
    --brand-orange: #ef6c22;
    --silver: #9a9a9a;
    --back-light: #fbfbfb;
    --back-edge: #dcdcdc;
  }
  * { margin: 0; padding: 0; box-sizing: border-box; }
  html, body {
    width: 1200px; height: 1096px; overflow: hidden;
    background: var(--bg);
  }
  .sheet { position: relative; width: 1200px; height: 1096px; }
  .card {
    position: absolute; left: 160px; width: 880px; height: 503px;
    overflow: hidden; box-shadow: 0 6px 18px rgba(0,0,0,0.18);
  }
  .card--front { top: 30px; background: var(--card-white); }
  .card--back {
    top: 563px;
    background: radial-gradient(ellipse at 50% 45%, var(--back-light) 30%, var(--back-edge) 100%);
  }

  /* Front */
  .side-band {
    position: absolute; left: 0; top: 0; width: 150px; height: 100%;
    background: var(--brand-blue);
  }
  .contact-panel {
    position: absolute; left: 42px; top: 262px; width: 460px; height: 200px;
    background: var(--card-white); border-radius: 26px 0 0 26px;
  }
  .brand {
    display: flex; align-items: center;
    font-family: 'Jost', sans-serif; font-weight: 700; color: var(--brand-blue);
  }
  .card--front .brand { position: absolute; left: 180px; top: 52px; gap: 14px; }
  .brand-mark { flex: none; border-radius: 50%; background: var(--silver); }
  .card--front .brand-mark { width: 54px; height: 54px; }
  .brand-name { line-height: 1.05; letter-spacing: 0.5px; white-space: nowrap; }
  .card--front .brand-name { font-size: 27px; }

  .person {
    position: absolute; left: 180px; top: 170px;
    font-family: 'Arimo', sans-serif;
  }
  .person-name { font-size: 24px; font-weight: 700; color: var(--brand-blue); }
  .person-title { font-size: 16px; color: var(--brand-orange); margin-top: 4px; }

  .contacts {
    position: absolute; left: 74px; top: 284px; list-style: none;
    font-family: 'Arimo', sans-serif; font-size: 21px; color: var(--brand-blue);
  }
  .contacts li { display: flex; align-items: center; gap: 14px; height: 36px; }
  .contacts svg { width: 22px; height: 22px; flex: none; }

  .membership {
    position: absolute; right: 36px; bottom: 56px;
    display: flex; align-items: center; gap: 12px;
    font-family: 'Arimo', sans-serif; font-size: 15px; color: var(--brand-blue);
  }
  .member-badge { width: 26px; height: 26px; background: var(--brand-blue); border-radius: 3px; }

  /* Back */
  .back-lockup {
    position: absolute; left: 0; right: 0; top: 50%; transform: translateY(-50%);
    display: flex; flex-direction: column; align-items: center; gap: 18px;
  }
  .card--back .brand { flex-direction: column; gap: 16px; text-align: center; }
  .card--back .brand-mark { width: 90px; height: 90px; }
  .card--back .brand-name { font-size: 46px; }
  .byline {
    font-family: 'Arimo', sans-serif; font-size: 24px; font-weight: 700;
    color: var(--brand-orange); letter-spacing: 0.3px;
  }
</style>
</head>
<body>
<main class="sheet">
  <section class="card card--front" aria-label="Business card front">
    <div class="side-band"></div>
    <div class="contact-panel"></div>

    <div class="brand">
      <span class="brand-mark"></span>
      <div class="brand-name">MORWEN CRAFTWORKS<br>SOLUTIONS PTY LTD.</div>
    </div>

    <div class="person">
      <p class="person-name">Your Name Here</p>
      <p class="person-title">Position</p>
    </div>

    <ul class="contacts">
      <li>
        <svg viewBox="0 0 24 24" aria-hidden="true"><path fill="var(--brand-orange)" d="M6.6 10.8a15 15 0 0 0 6.6 6.6l2.2-2.2a1 1 0 0 1 1-.25 11.4 11.4 0 0 0 3.6.57 1 1 0 0 1 1 1V20a1 1 0 0 1-1 1A17 17 0 0 1 3 4a1 1 0 0 1 1-1h3.5a1 1 0 0 1 1 1c0 1.25.2 2.45.57 3.57a1 1 0 0 1-.25 1z"/></svg>
        612-480-3391
      </li>
      <li>
        <svg viewBox="0 0 24 24" aria-hidden="true"><g fill="var(--brand-orange)"><rect x="6" y="2" width="12" height="6"/><rect x="2" y="9" width="20" height="9" rx="2"/><rect x="6" y="15" width="12" height="7" fill="#fff" stroke="var(--brand-orange)" stroke-width="2"/></g></svg>
        612-480-3392
      </li>
      <li>
        <svg viewBox="0 0 24 24" aria-hidden="true"><rect x="2" y="5" width="20" height="14" fill="var(--brand-orange)"/><path d="M2 5l10 8 10-8" fill="none" stroke="#fff" stroke-width="1.8"/></svg>
        hello@morwencraftworks.com.au
      </li>
      <li>
        <svg viewBox="0 0 24 24" aria-hidden="true"><g fill="none" stroke="var(--brand-orange)" stroke-width="2"><circle cx="12" cy="12" r="9.5"/><ellipse cx="12" cy="12" rx="4" ry="9.5"/><path d="M2.5 12h19"/></g></svg>
        www.morwencraftworks.com.au
      </li>
    </ul>

    <div class="membership">
      <span>Member of the NHG</span>
      <span class="member-badge" role="img" aria-label="Northern Homecraft Guild membership badge"></span>
    </div>
  </section>

  <section class="card card--back" aria-label="Business card back">
    <div class="back-lockup">
      <div class="brand">
        <span class="brand-mark"></span>
        <div class="brand-name">MORWEN CRAFTWORKS<br>SOLUTIONS PTY LTD.</div>
      </div>
      <p class="byline">Our Business is Building!</p>
    </div>
  </section>
</main>
</body>
</html>
```